Email Signature

We need a generic email signature designed for our buiding company called 'Birchfield Dwellings'.
We need the following included:
- Name
- Job title (Sales Consultant)
- Phone number
- Mobile number
- Email address
- Physical address
- Web addresss
Please look at the files I have uploaded as these will give you a good idea on our current branding. Our current email signature works well but just needs refreshing! I've also uploaded some images which can be used if needed.
Industry/Entity Type
It Company
Requirements
Nice to have
- If you could incorporate the colours used on the brochure example (contents list) and and arrows on the bottom of the letterhead... just a thought!

```html
<!DOCTYPE html>
<html lang="en">
<head>
<meta charset="utf-8">
<title>Birchfield Dwellings — Email Signature</title>
<link href="https://fonts.googleapis.com/css2?family=Arimo:wght@400;700&display=swap" rel="stylesheet">
<style>
  :root {
    --brand-red: #b5121b;
    --rule-dark: #8c2a3a;
    --ink: #111111;
    --frame: #c4c4c4;
    --page: #ffffff;
    --social-a: #3b5998;
    --social-b: #4a79a8;
    --social-c: #c9a27a;
    --social-d: #4fb3e8;
    --social-e: #2d8fc4;
  }
  html, body {
    margin: 0;
    padding: 0;
    width: 1200px;
    height: 1000px;
    overflow: hidden;
    background: var(--page);
    font-family: "Arimo", Arial, sans-serif;
  }
  .canvas {
    position: relative;
    width: 1200px;
    height: 1000px;
  }
  .signature {
    position: absolute;
    left: 57px;
    top: 348px;
    width: 1082px;
    height: 246px;
    border: 1.5px dashed var(--frame);
  }
  .person-name {
    position: absolute;
    left: 34px;
    top: 10px;
    margin: 0;
    font-size: 29px;
    font-weight: 400;
    color: var(--brand-red);
  }
  .person-title {
    position: absolute;
    left: 35px;
    top: 45px;
    margin: 0;
    font-size: 16px;
    color: var(--ink);
  }
  .brand {
    position: absolute;
    left: 110px;
    top: 96px;
    display: flex;
    align-items: center;
    gap: 12px;
  }
  .brand-mark {
    width: 40px;
    height: 40px;
    background: var(--brand-red);
  }
  .brand-name {
    font-size: 32px;
    font-weight: 400;
    color: var(--brand-red);
    white-space: nowrap;
  }
  .divider {
    position: absolute;
    left: 531px;
    top: 69px;
    width: 3px;
    height: 98px;
    background: var(--brand-red);
  }
  .contact {
    position: absolute;
    left: 596px;
    top: 56px;
    margin: 0;
    font-size: 17px;
    color: var(--ink);
    line-height: 1;
  }
  .contact p { margin: 0; position: absolute; white-space: nowrap; }
  .contact .label { color: var(--brand-red); }
  .contact .address { top: 0; }
  .contact .phone { top: 24px; }
  .contact .mobile { top: 47px; }
  .contact .email { top: 77px; }
  .contact .web { top: 101px; }
  .rule {
    position: absolute;
    left: 22px;
    width: 1038px;
    height: 1px;
  }
  .rule-top { top: 196px; background: var(--rule-dark); }
  .rule-bottom { top: 231px; background: var(--brand-red); }
  .social {
    position: absolute;
    left: 28px;
    top: 202px;
    display: flex;
    gap: 10px;
    margin: 0;
    padding: 0;
    list-style: none;
  }
  .social li {
    width: 23px;
    height: 23px;
    border-radius: 2px;
  }
  .social .s1 { background: var(--social-a); }
  .social .s2 { background: var(--social-b); }
  .social .s3 { background: var(--social-c); }
  .social .s4 { background: var(--social-d); }
  .social .s5 { background: var(--social-e); }
</style>
</head>
<body>
<div class="canvas">
  <section class="signature">
    <h1 class="person-name">Jordan Ashby</h1>
    <p class="person-title">Sales Consultant</p>

    <div class="brand">
      <span class="brand-mark"></span>
      <span class="brand-name">Birchfield Dwellings</span>
    </div>

    <div class="divider"></div>

    <div class="contact">
      <p class="address">18 Mill Street ( Coast Hwy ), Kelso VIC 3871</p>
      <p class="phone"><span class="label">Phone :</span>&nbsp; 03 5550 1234</p>
      <p class="mobile"><span class="label">Mob :</span>&nbsp; 0400 555 218</p>
      <p class="email"><span class="label">Email :</span> jordan@birchfielddwellings.com.au</p>
      <p class="web">www.birchfielddwellings.com.au</p>
    </div>

    <div class="rule rule-top"></div>
    <ul class="social" aria-label="Social media links">
      <li class="s1"></li>
      <li class="s2"></li>
      <li class="s3"></li>
      <li class="s4"></li>
      <li class="s5"></li>
    </ul>
    <div class="rule rule-bottom"></div>
  </section>
</div>
</body>
</html>
```